Business Card Design

I need a business card designed for my business.

The company name is Miles Renford Collective

It has four brands underneath it. They are:
- MR Occasions
- MR Athletic Journeys
- MRC Stewardship
- Dove Draftworks

I have attached all logo items, as well as our last business card.

I look forward to seeing your designs.

Industry/Entity Type

Business

Colors
eb1f27
0355a3

Requirements
Must have
• Our contact details as per the front page of our previous business card.

```html
<!DOCTYPE html>
<html lang="en">
<head>
<meta charset="utf-8">
<title>Miles Renford Collective – Business Card</title>
<link rel="stylesheet" href="https://fonts.googleapis.com/css2?family=Arimo:wght@700&family=Russo+One&family=Lobster+Two:ital,wght@1,700&display=swap">
<style>
  :root {
    --brand-red: #eb1f27;
    --brand-blue: #0355a3;
    --front-blue: #3a44f2;
    --back-red: #c8161c;
    --ink: #111111;
    --white: #ffffff;
    --edge: #8a8a8a;
  }
  html, body {
    margin: 0;
    padding: 0;
    width: 1032px;
    height: 1200px;
    overflow: hidden;
    background: var(--white);
  }
  .canvas {
    position: relative;
    width: 1032px;
    height: 1200px;
    font-family: "Arimo", Arial, sans-serif;
  }
  .card {
    position: absolute;
    left: 0;
    width: 1030px;
    border: 1px solid var(--edge);
    overflow: hidden;
  }
  .card--front {
    top: 0;
    height: 588px;
    background: linear-gradient(to bottom, var(--white) 0%, var(--white) 24%, #c9ccfb 48%, #7d84f6 72%, var(--front-blue) 100%);
  }
  .card--back {
    top: 606px;
    height: 592px;
    background: linear-gradient(to bottom, var(--white) 0%, #f6dcdd 30%, #e47d81 62%, var(--back-red) 100%);
  }

  /* Front */
  .company-mark {
    position: absolute;
    left: 60px;
    top: 32px;
    width: 208px;
    height: 208px;
    border-radius: 50%;
    background: var(--brand-blue);
  }
  .company-name {
    position: absolute;
    left: 300px;
    top: 46px;
    margin: 0;
    font-size: 74px;
    line-height: 86px;
    font-weight: 700;
    color: var(--brand-blue);
    letter-spacing: -1px;
  }
  .holder {
    position: absolute;
    left: 0;
    width: 1030px;
    top: 248px;
    text-align: center;
    font-family: "Russo One", sans-serif;
    font-style: italic;
    color: var(--ink);
  }
  .holder__name {
    margin: 0;
    font-size: 54px;
    line-height: 62px;
    letter-spacing: 3px;
  }
  .holder__role {
    margin: 0;
    font-size: 34px;
    line-height: 42px;
    letter-spacing: 2px;
  }
  .contact {
    position: absolute;
    margin: 0;
    color: var(--white);
    font-size: 28px;
    line-height: 39px;
    font-style: normal;
  }
  .contact--address { left: 32px; top: 380px; }
  .contact--phones { right: 28px; top: 399px; text-align: right; }
  .contact--email, .contact--web {
    top: 543px;
    font-size: 24px;
    line-height: 30px;
  }
  .contact--email { left: 32px; }
  .contact--web { right: 28px; }

  /* Back */
  .brand {
    position: absolute;
    margin: 0;
    font-size: 46px;
    line-height: 52px;
    font-weight: 700;
    display: flex;
    align-items: center;
    gap: 16px;
  }
  .brand--blue { color: var(--brand-blue); }
  .brand--red { color: var(--brand-red); }
  .brand__dot {
    flex: none;
    width: 40px;
    height: 40px;
    border-radius: 50%;
    background: currentColor;
  }
  .brand--stewardship { left: 44px; top: 56px; }
  .brand--draftworks { right: 56px; top: 56px; }
  .brand--occasions { left: 40px; top: 234px; }
  .brand--journeys { right: 44px; top: 234px; font-size: 40px; }

  .tagline {
    position: absolute;
    left: 0;
    width: 1030px;
    top: 376px;
    margin: 0;
    text-align: center;
    font-family: "Lobster Two", cursive;
    font-style: italic;
    font-weight: 700;
    font-size: 50px;
    line-height: 60px;
    color: var(--white);
    letter-spacing: 1px;
    -webkit-text-stroke: 2px var(--ink);
    text-shadow: 3px 3px 0 var(--brand-red), 4px 4px 0 var(--ink);
  }
  .web-icon {
    position: absolute;
    left: 48px;
    top: 474px;
    width: 116px;
    height: 116px;
    border-radius: 50%;
    background: radial-gradient(circle at 38% 35%, #d9ecff 0%, #5aa2e6 45%, #1b5fb0 100%);
  }
  .web-address {
    position: absolute;
    left: 188px;
    top: 508px;
    margin: 0;
    font-size: 38px;
    line-height: 46px;
    color: var(--white);
    letter-spacing: 2px;
    text-shadow: 2px 2px 0 var(--ink);
  }
</style>
</head>
<body>
<main class="canvas">

  <section class="card card--front" aria-label="Business card front">
    <div class="company-mark" aria-hidden="true"></div>
    <h1 class="company-name">Miles Renford<br>Collective</h1>

    <div class="holder">
      <p class="holder__name">Miles Renford</p>
      <p class="holder__role">Principal</p>
    </div>

    <address class="contact contact--address">PO Box 418<br>Carrow ACT 2609<br>Australia</address>
    <p class="contact contact--phones">+61 2 6200 4185<br>+61 455 302 817</p>
    <p class="contact contact--email">Miles@MRCollective.com.au</p>
    <p class="contact contact--web">www.MRCollective.com.au</p>
  </section>

  <section class="card card--back" aria-label="Business card back">
    <p class="brand brand--blue brand--stewardship"><span class="brand__dot" aria-hidden="true"></span>MRC Stewardship</p>
    <p class="brand brand--red brand--draftworks">Dove Draftworks<span class="brand__dot" aria-hidden="true"></span></p>
    <p class="brand brand--blue brand--occasions"><span class="brand__dot" aria-hidden="true"></span>MR Occasions</p>
    <p class="brand brand--red brand--journeys">MR Athletic Journeys</p>

    <p class="tagline">Event, travel and talent management</p>

    <div class="web-icon" role="img" aria-label="Globe web icon"></div>
    <p class="web-address">www.MRCollective.com.au</p>
  </section>

</main>
</body>
</html>
```